Harbor Fieldworks (Business Card Design)

Need business cards designed. Something modern, chic, and sleek. Mabye the back of the card should be the navy blue that is in the logo and then just the logo on the back.

Target Market(s)

Those in the hotel, office, and renovation industry

Contact Information for Business Card

1. Logo 2. Dorian Velasko 3. CEO/Founder 4. Phone: (833) HarbFld / (833) 427-2353 5. Email: dorian@theharborfieldworks.com 6. Website: www.theharborfieldworks.com

Font styles to use
Other font styles liked:
• Look at the logo font and base the font for everything else off of that.

Colors
0054AA
0677BA
7BADD7
CADEEF
E8F1F8

Requirements
Must have
• Colors that are associated in the logo
Nice to have
• Sleek modern clean and chic design.

```html
<!DOCTYPE html>
<html lang="en">
<head>
<meta charset="utf-8">
<title>Harbor Fieldworks – Business Card</title>
<link rel="stylesheet" href="https://fonts.googleapis.com/css2?family=Montserrat:wght@400;500;600;700&display=swap">
<style>
  :root {
    --navy: #131b45;
    --navy-soft: #1b2554;
    --gold: #c9a13a;
    --paper: #ffffff;
    --paper-shade: #f1f1f3;
    --ink: #4a4a52;
    --backdrop: #dcdde0;
  }
  * { box-sizing: border-box; margin: 0; padding: 0; }
  html, body {
    width: 1200px; height: 800px; overflow: hidden;
    background: var(--backdrop);
    font-family: "Montserrat", sans-serif;
  }
  .stage { position: relative; width: 1200px; height: 800px; }
  .card {
    position: absolute; top: 246px;
    width: 540px; height: 308px;
    overflow: hidden;
    box-shadow: 0 6px 18px rgba(0,0,0,0.12);
  }
  .card-back { left: 40px; background: var(--navy); }
  .card-front { left: 620px; background: var(--paper); }

  .pattern-field { position: absolute; inset: 0; }
  .card-back .pattern-field {
    background: linear-gradient(135deg, var(--navy) 0%, var(--navy-soft) 50%, var(--navy) 100%);
  }
  .card-front .pattern-field {
    background: linear-gradient(135deg, var(--paper) 0%, var(--paper-shade) 50%, var(--paper) 100%);
  }

  .brand {
    position: absolute; left: 0; right: 0; top: 50%;
    transform: translateY(-50%);
    display: flex; align-items: center; justify-content: center; gap: 14px;
  }
  .brand-square { width: 30px; height: 30px; }
  .brand-name {
    font-weight: 600; font-size: 30px; letter-spacing: 3px;
    text-transform: uppercase; white-space: nowrap;
  }
  .card-back .brand-square { background: var(--paper); }
  .card-back .brand-name { color: var(--paper); }
  .card-front .brand-square { background: var(--navy); }
  .card-front .brand-name { color: var(--navy); }

  .identity { position: absolute; left: 28px; top: 24px; }
  .identity-name {
    font-weight: 700; font-size: 13px; color: var(--navy);
    text-transform: uppercase; letter-spacing: 0.3px;
  }
  .identity-role { font-weight: 400; color: var(--ink); text-transform: none; }
  .contact-line {
    display: flex; align-items: center; gap: 6px;
    font-size: 11px; color: var(--ink); margin-top: 5px;
  }
  .contact-icon { width: 11px; height: 11px; flex: none; }
  .contact-block {
    position: absolute; right: 28px; bottom: 24px;
    display: flex; flex-direction: column; align-items: flex-end;
  }
  .contact-block .contact-line { flex-direction: row; }
</style>
</head>
<body>
<main class="stage">
  <section class="card card-back" aria-label="Card back">
    <div class="pattern-field" role="img" aria-label="Faint large chevron pattern in navy tones"></div>
    <div class="brand">
      <span class="brand-square"></span>
      <span class="brand-name">Harbor Fieldworks</span>
    </div>
  </section>

  <section class="card card-front" aria-label="Card front">
    <div class="pattern-field" role="img" aria-label="Faint large chevron pattern in light grey tones"></div>

    <div class="identity">
      <p class="identity-name">Dorian Velasko | <span class="identity-role">CEO/Founder</span></p>
      <p class="contact-line">
        <svg class="contact-icon" viewBox="0 0 12 12" aria-hidden="true"><path fill="#c9a13a" d="M2.5 1l2 .3.7 2.4-1.2.9a7 7 0 0 0 3.4 3.4l.9-1.2 2.4.7.3 2c-.4.6-1 .9-1.7.9A8.5 8.5 0 0 1 1 2.7c0-.7.5-1.3 1.5-1.7z"/></svg>
        (833) HarbFld / (833) 427-2353
      </p>
    </div>

    <div class="brand">
      <span class="brand-square"></span>
      <span class="brand-name">Harbor Fieldworks</span>
    </div>

    <div class="contact-block">
      <p class="contact-line">dorian@theharborfieldworks.com
        <svg class="contact-icon" viewBox="0 0 12 12" aria-hidden="true"><rect x="1" y="2.5" width="10" height="7" rx="1" fill="#c9a13a"/><path d="M1.5 3l4.5 3.5L10.5 3" fill="none" stroke="#fff" stroke-width="1"/></svg>
      </p>
      <p class="contact-line">www.theharborfieldworks.com
        <svg class="contact-icon" viewBox="0 0 12 12" aria-hidden="true"><circle cx="6" cy="6" r="5" fill="none" stroke="#c9a13a" stroke-width="1.2"/><ellipse cx="6" cy="6" rx="2" ry="5" fill="none" stroke="#c9a13a" stroke-width="1"/><path d="M1 6h10" stroke="#c9a13a" stroke-width="1"/></svg>
      </p>
    </div>
  </section>
</main>
</body>
</html>
```